Business Card Design

We need a business card designed for a new company based in Melbourne called Korvum solutions. Korvum solutions provides management consulting specialising in the health and social services sector.

Korvum solutions offer a unique set of specialist skills │dealing with all levels of government │ unique communication skills│intimate knowledge of the health sector │solutions tailored to unique circumstances.

Korvum solutions takes on a select number of clients at any one time, this ensures that your organisation receives the attention required. On larger projects, Korvum solutions join up with other consultants to bring specialist skills to a project.
Updates

This is the first time I have used Pixel Bazaar and thank you all for responding. The variation is amazing and makes it hard to decide. I have to ask some of my friends to give me their views. The response is fantastic. The one I pick will basically be the most visually appealing

Industry/Entity Type

Management Consulting

Contact Information for Business Card

Marcus Pellow, Principal, Korvum solutions, 14 Wexcombe Ave, Dunlarry VIC 3999, 0400 137 284, marcusp@korvumsolutions.example, www.korvumsolutions.example

```html
<!DOCTYPE html>
<html lang="en">
<head>
<meta charset="utf-8">
<title>Korvum solutions – Business Card</title>
<link href="https://fonts.googleapis.com/css2?family=Arimo:ital,wght@0,400;0,700;1,700&display=swap" rel="stylesheet">
<style>
  :root {
    --brand-red: #bf0017;
    --ink: #111111;
    --card: #ffffff;
    --backdrop: #e9e6e1;
    --band: #000000;
  }
  html, body {
    margin: 0;
    padding: 0;
    width: 1200px;
    height: 798px;
    overflow: hidden;
    background: var(--backdrop);
  }
  .card {
    position: absolute;
    left: 107px;
    top: 94px;
    width: 986px;
    height: 609px;
    background: var(--card);
    font-family: "Arimo", Arial, sans-serif;
    color: var(--ink);
  }
  .brand-tab {
    position: absolute;
    left: 0;
    top: 209px;
    width: 506px;
    height: 191px;
    background: var(--brand-red);
    border-radius: 0 100px 100px 0;
  }
  .brand-name {
    position: absolute;
    left: 90px;
    top: 58px;
    margin: 0;
    font-size: 40px;
    font-weight: 700;
    line-height: 1;
    color: #ffffff;
    letter-spacing: 0.5px;
  }
  .brand-tagline {
    position: absolute;
    left: 142px;
    top: 126px;
    margin: 0;
    font-size: 12px;
    font-weight: 700;
    line-height: 1;
    color: #ffffff;
    letter-spacing: 0.6px;
    text-transform: uppercase;
  }
  .contact-block {
    position: absolute;
    right: 62px;
    top: 397px;
    text-align: right;
  }
  .person-name {
    margin: 0;
    font-size: 27px;
    font-weight: 400;
    line-height: 32px;
    color: var(--brand-red);
    word-spacing: 4px;
  }
  .person-role {
    margin: 0;
    font-size: 24px;
    font-weight: 700;
    font-style: italic;
    line-height: 30px;
  }
  .address {
    margin: 20px 0 0;
    font-size: 17px;
    line-height: 22px;
    word-spacing: 2px;
  }
  .contact-line {
    margin: 0;
    font-size: 17px;
    line-height: 22px;
    display: flex;
    justify-content: flex-end;
    align-items: center;
    gap: 8px;
    word-spacing: 3px;
  }
  .contact-line .icon {
    width: 16px;
    height: 16px;
    flex: none;
  }
  .contact-line .item + .icon {
    margin-left: 6px;
  }
  .base-band {
    position: absolute;
    left: 0;
    top: 568px;
    width: 986px;
    height: 26px;
    background: var(--band);
  }
</style>
</head>
<body>
  <main class="card">
    <div class="brand-tab">
      <h1 class="brand-name">Korvum solutions</h1>
      <p class="brand-tagline">Health &amp; Social Services Consulting</p>
    </div>

    <section class="contact-block">
      <h2 class="person-name">Marcus Pellow</h2>
      <p class="person-role">Principal</p>
      <p class="address">14 Wexcombe Ave. Dunlarry VIC 3999</p>
      <p class="contact-line">
        <svg class="icon" viewBox="0 0 16 16" aria-hidden="true">
          <rect x="5" y="2" width="6" height="12" rx="1" fill="none" stroke="#111" stroke-width="1.2"/>
          <line x1="7" y1="12" x2="9" y2="12" stroke="#111" stroke-width="1"/>
        </svg>
        <span class="item">0400 137 284</span>
        <svg class="icon" viewBox="0 0 16 16" aria-hidden="true">
          <rect x="2" y="4" width="12" height="8" fill="none" stroke="#111" stroke-width="1.2"/>
          <polyline points="2,4 8,9 14,4" fill="none" stroke="#111" stroke-width="1.2"/>
        </svg>
        <span class="item">marcusp@korvumsolutions.example</span>
        <svg class="icon" viewBox="0 0 16 16" aria-hidden="true">
          <circle cx="8" cy="8" r="6.5" fill="none" stroke="#111" stroke-width="1.2"/>
          <ellipse cx="8" cy="8" rx="2.8" ry="6.5" fill="none" stroke="#111" stroke-width="0.9"/>
          <line x1="1.5" y1="8" x2="14.5" y2="8" stroke="#111" stroke-width="0.9"/>
        </svg>
        <span class="item">www.korvumsolutions.example</span>
      </p>
    </section>

    <div class="base-band"></div>
  </main>
</body>
</html>
```